web design needed for brivolent safety ltd

We need a web design for our new company. It is called Brivo Lent Safety Ltd and is a company based around a security/safety/info box specifically made for on construction sites, but could be used elsewhere. It is completely portable with a builtin alarm system with remote. There is a larger box and a smaller box (only have an image for this one at this stage, I will get better photos of the temp box soon, but this one will make a start).
This will be the standard box that is for sale, howver you can get upgrades that include a fire extinguisher, first aid kit, hand sanitizer, fire blanket.
Other features include a place for plans and safety info for the site, a hook attached to the back of the smaller box so it can be hung on the door. Both boxes are suitable for outside.
We would like the wesite to incorporate our logo and pictures of the box. I have attached our logo and an exaple of a mock box as the final box is still being made sothese photos will be swapped once we have it from the manufacturer.
We would like the following pages:
Home (possibly a picture of the box rotating, doesnt have to though?)
About us
Products
FAQ
Shopping cart
Contact us
We would like the style to be crisp, simple and not to busy.
Thanks
Updates
More photos of the box have been added. These are for the larger box.
Reason: we are happy to give people more time so have extended it by seven days
Target Market(s)
Builders mainly
Industry/Entity Type
Construction
Font styles to use
Other font styles liked:
- ERAS BOLD ITC
Look and feel
Each slider illustrates characteristics of the customer's brand and the style your logo design should communicate.

```html
<!DOCTYPE html>
<html lang="en">
<head>
<meta charset="utf-8">
<title>Brivo Lent Safety Ltd</title>
<link href="https://fonts.googleapis.com/css2?family=Ubuntu:ital,wght@0,400;0,500;0,700;1,400&family=Open+Sans:wght@400;600&display=swap" rel="stylesheet">
<style>
:root{
  --green:#8cbd33;
  --green-dark:#6d9a1f;
  --blue:#3f9bd4;
  --teal:#3a98b5;
  --red:#e2263a;
  --ink:#1e1e1e;
  --band:#e5e5e5;
  --text:#6f6f6f;
  --line:#d8d8d8;
  --white:#ffffff;
  --footer:#1c1c1c;
}
*{margin:0;padding:0;box-sizing:border-box}
html,body{width:1200px;height:1041px;overflow:hidden;background:var(--white)}
body{position:relative;font-family:"Open Sans",sans-serif;color:var(--text)}
a{text-decoration:none;color:inherit}
.abs{position:absolute}

.hero-bg{left:0;top:0;width:1200px;height:440px}
.band{left:0;top:400px;width:1200px;height:335px;background:var(--band)}

.site-header{left:180px;top:0;width:839px;height:72px;background:var(--white)}
.brand{left:26px;top:12px;display:flex;align-items:center;gap:10px;font-family:"Ubuntu",sans-serif;font-weight:700;font-size:19px;line-height:20px;color:var(--green)}
.brand-square{width:44px;height:44px;background:var(--green);border-radius:6px}
.main-nav{right:0;top:0;display:flex;height:72px}
.main-nav a{display:flex;align-items:center;justify-content:center;height:72px;padding:0 17px;border-top:4px solid;border-left:1px solid #ececec;font-family:"Ubuntu",sans-serif;font-weight:700;font-size:13px;color:var(--ink)}
.main-nav a:first-child{border-left:none;color:var(--blue);font-weight:500}

.hero-visual{left:180px;top:125px;width:450px;height:240px;background:linear-gradient(135deg,#e0195e,#b80f48);border-radius:4px}
.hero-title{left:661px;top:120px;font-family:"Ubuntu",sans-serif;font-weight:700;font-size:30px;line-height:35px;color:var(--white)}
.hero-copy{left:663px;top:203px;width:330px;font-family:"Ubuntu",sans-serif;font-size:10px;line-height:15.5px;color:#cfcfcf;text-transform:uppercase}
.btn-more{left:663px;top:292px;display:flex;height:37px}
.btn-more span{width:103px;background:var(--white);display:flex;align-items:center;justify-content:center;font-family:"Ubuntu",sans-serif;font-size:16px;color:var(--ink)}
.btn-more i{width:35px;background:var(--teal);display:flex;align-items:center;justify-content:center}

.side-tab{background:linear-gradient(90deg,#d9d9d9,#f3f3f3);display:flex;align-items:center;justify-content:center}
.side-tab b{transform:rotate(-90deg);white-space:nowrap;font-family:"Ubuntu",sans-serif;font-weight:400;color:var(--ink)}
.features-tab{left:180px;top:397px;width:52px;height:246px}
.features-tab b{font-size:25px}

.card{top:391px;height:270px;background:var(--white);border:1px solid var(--line);padding:4px}
.card-photo{height:126px}
.card h3{margin:8px 10px 0;padding-bottom:4px;border-bottom:1px solid var(--line);font-family:"Ubuntu",sans-serif;font-weight:500;font-size:17px;color:var(--green-dark)}
.card p{margin:6px 10px 0;font-size:10px;line-height:15.5px}

.testimonial{left:811px;top:393px;width:207px;height:239px;background:var(--green);padding:12px 14px;color:var(--white)}
.testimonial h4{font-family:"Ubuntu",sans-serif;font-weight:400;font-size:19px}
.t-arrows{right:10px;top:14px;display:flex;gap:5px}
.t-arrows span{width:19px;height:19px;border:1.5px solid var(--white);border-radius:50%;display:flex;align-items:center;justify-content:center}
.testimonial blockquote{margin-top:14px;font-family:"Ubuntu",sans-serif;font-style:italic;font-size:11px;line-height:18.5px}
.testimonial cite{display:block;margin-top:12px;font-style:normal;font-family:"Ubuntu",sans-serif;font-size:14px}
.testimonial small{display:block;font-size:9.5px;margin-top:-1px}
.t-pointer{left:975px;top:632px;width:0;height:0;border-left:7px solid transparent;border-right:7px solid transparent;border-top:8px solid var(--green)}
.avatar{left:962px;top:645px;width:46px;height:46px;border-radius:50%;background:linear-gradient(#c9d3dc,#9aa7b3);border:3px solid var(--white);box-shadow:0 0 0 1px #cfd6dc}

.clients{left:180px;top:706px;width:839px;height:100px;background:var(--white);border:1px solid var(--line)}
.clients-tab{left:180px;top:706px;width:50px;height:100px}
.clients-tab b{font-size:19px}
.client-list{left:250px;top:706px;width:760px;height:100px;display:flex;align-items:center;justify-content:space-around}
.client-list span{font-family:"Ubuntu",sans-serif;font-weight:500;font-size:17px;color:#3c3c3c}

.site-footer{left:180px;top:833px;width:839px;height:208px;background:var(--green)}
.footer-nav{left:19px;top:0;height:55px;display:flex;align-items:center;gap:27px}
.footer-nav a{font-family:"Ubuntu",sans-serif;font-size:12px;color:var(--white)}
.newsletter{left:522px;top:17px;display:flex;align-items:center}
.newsletter label{font-family:"Ubuntu",sans-serif;font-size:14px;color:#3f5a14;margin-right:10px}
.newsletter .field{width:205px;height:24px;background:var(--white);border:2px solid #dfe9cc;display:flex;justify-content:space-between;align-items:center;padding-left:8px;font-size:10px;color:#9a9a9a}
.newsletter .field b{background:var(--blue);color:var(--white);font-weight:400;font-size:11px;height:18px;width:32px;display:flex;align-items:center;justify-content:center;margin-right:1px}
.footer-panel{left:8px;top:52px;width:823px;height:148px;background:var(--footer)}
.footer-brand{left:40px;top:28px;display:flex;align-items:center;gap:10px;font-family:"Ubuntu",sans-serif;font-weight:700;font-size:19px;line-height:20px;color:var(--green)}
.copyright{left:38px;top:102px;font-size:11px;line-height:15px;color:#6a6a6a}
.copyright strong{color:var(--white);font-weight:400}
.contact-list{left:362px;top:34px;width:376px}
.contact-list li{list-style:none;display:flex;align-items:center;height:26px;border-bottom:1px solid #3a3a3a;font-family:"Ubuntu",sans-serif;font-size:12px;color:var(--white)}
.contact-list li:last-child{border-bottom:none}
.contact-list .lbl{display:flex;align-items:center;gap:7px;width:215px;flex:none}
.contact-list .val{white-space:nowrap}
</style>
</head>
<body>

<svg class="abs hero-bg" viewBox="0 0 1200 440" aria-hidden="true">
  <defs>
    <radialGradient id="heroGlow" cx="50%" cy="30%" r="70%">
      <stop offset="0" stop-color="#3a3a3f"/>
      <stop offset="1" stop-color="#232326"/>
    </radialGradient>
  </defs>
  <rect width="1200" height="440" fill="url(#heroGlow)"/>
  <path d="M0 398 Q600 455 1200 398 L1200 440 L0 440Z" fill="#e5e5e5"/>
</svg>
<div class="abs band"></div>

<header class="abs site-header">
  <div class="abs brand"><span class="brand-square"></span><span>BRIVO LENT<br>SAFETY</span></div>
  <nav class="abs main-nav">
    <a href="#" style="border-top-color:var(--blue)">HOME</a>
    <a href="#" style="border-top-color:var(--green)">ABOUT US</a>
    <a href="#" style="border-top-color:var(--green)">PRODUCTS</a>
    <a href="#" style="border-top-color:var(--teal)">FAQ</a>
    <a href="#" style="border-top-color:var(--red)">SHOPPING CART</a>
    <a href="#" style="border-top-color:var(--ink)">CONTACT US</a>
  </nav>
</header>

<div class="abs hero-visual" role="img" aria-label="Photo of the open red site safety box with plans, first aid kit and fire extinguisher"></div>
<h1 class="abs hero-title">LOREM IPSUM<br>DOLOR SIT AMET</h1>
<p class="abs hero-copy">Lorem Ipsum is simply dummy text of the printing and type-setting industry. Lorem Ipsum has been the industry's stan-dard dummy text ever since the 1500s, when an unknown printer took a galley of type and scrambled it to make a type specimen book.</p>
<a class="abs btn-more" href="#"><span>Read more</span><i><svg width="12" height="16" viewBox="0 0 12 16"><path d="M3 2l6 6-6 6" fill="none" stroke="#fff" stroke-width="2.5"/></svg></i></a>

<div class="abs side-tab features-tab"><b>Our Features</b></div>

<article class="abs card" style="left:232px;width:187px">
  <div class="card-photo" role="img" aria-label="Photo of hand sanitizer bottles" style="background:linear-gradient(#f4f7f7,#7fc9cf)"></div>
  <h3>Hand sanitizer</h3>
  <p>Lorem Ipsum is simply dummy text of the printing and typeset-ting industry. Lorem Ipsum has been the industry's standard dummy text ever since the 1500s.</p>
</article>
<article class="abs card" style="left:430px;width:179px">
  <div class="card-photo" role="img" aria-label="Photo of a white first aid kit case" style="background:linear-gradient(#e9e9ea,#cfd0d3)"></div>
  <h3>First aid kit</h3>
  <p>Lorem Ipsum is simply dummy text of the printing and typeset-ting industry. Lorem Ipsum has been the industry's standard dummy text ever since the 1500s.</p>
</article>
<article class="abs card" style="left:620px;width:179px">
  <div class="card-photo" role="img" aria-label="Photo of a red fire blanket pouch" style="background:linear-gradient(#dedede,#d23a2f 40%,#c22c24)"></div>
  <h3>Fire blanket</h3>
  <p>Lorem Ipsum is simply dummy text of the printing and typeset-ting industry. Lorem Ipsum has been the industry's standard dummy text ever since the 1500s.</p>
</article>

<aside class="abs testimonial">
  <h4>Testimonials</h4>
  <div class="abs t-arrows">
    <span><svg width="7" height="9" viewBox="0 0 7 9"><path d="M5 1L2 4.5 5 8" fill="none" stroke="#fff" stroke-width="1.5"/></svg></span>
    <span><svg width="7" height="9" viewBox="0 0 7 9"><path d="M2 1l3 3.5L2 8" fill="none" stroke="#fff" stroke-width="1.5"/></svg></span>
  </div>
  <blockquote>"Lorem Ipsum is simply dummy text of the printing and typesetting industry. Lorem Ipsum has been the industry's standard dummy text ever since the 1500s, when an unknown printer typesetting industry. Lorem Ipsum has been the industry's."</blockquote>
  <cite>-Corin Haldane</cite>
  <small>Ridgeway Builds</small>
</aside>
<div class="abs t-pointer"></div>
<div class="abs avatar" role="img" aria-label="Customer avatar placeholder"></div>

<section class="abs clients"></section>
<div class="abs side-tab clients-tab"><b>Clients</b></div>
<div class="abs client-list">
  <span>Harbourline</span>
  <span>Morrow &amp; Vale</span>
  <span>Kestrel</span>
  <span>Eastgate Institute</span>
  <span>Torvik</span>
</div>

<footer class="abs site-footer">
  <nav class="abs footer-nav">
    <a href="#">HOME</a><a href="#">ABOUT US</a><a href="#">PRODUCTS</a><a href="#">FAQ</a><a href="#">SHOPPING CART</a><a href="#">CONTACT US</a>
  </nav>
  <form class="abs newsletter">
    <label>Newsletter</label>
    <div class="field">your email<b>OK</b></div>
  </form>
  <div class="abs footer-panel">
    <div class="abs footer-brand"><span class="brand-square"></span><span>BRIVO LENT<br>SAFETY</span></div>
    <p class="abs copyright">© Copyright 2013 by <strong>Brivo Lent Safety</strong><br>All Right Reserved</p>
    <ul class="abs contact-list">
      <li><span class="lbl"><svg width="14" height="10" viewBox="0 0 14 10"><rect x=".5" y=".5" width="13" height="9" fill="none" stroke="#fff"/><path d="M.5 .5L7 6 13.5 .5" fill="none" stroke="#fff"/></svg>Mail</span><span class="val">hello@brivolentsafety.example</span></li>
      <li><span class="lbl"><svg width="14" height="12" viewBox="0 0 14 12"><path d="M3 1l2 3-1.5 1.5c1 2 2.5 3.5 4.5 4.5L9.5 8.5l3 2-1.5 1.5C6 11 2 7 1.5 2.5Z" fill="#fff"/></svg>Telephone</span><span class="val">021-555-0147</span></li>
      <li><span class="lbl"><svg width="14" height="12" viewBox="0 0 14 12"><rect x="3" y="0.5" width="8" height="4" fill="none" stroke="#fff"/><rect x="0.5" y="4" width="13" height="5" fill="none" stroke="#fff"/><rect x="3" y="7" width="8" height="4.5" fill="none" stroke="#fff"/></svg>Fax</span><span class="val">021 555 019 8410</span></li>
    </ul>
  </div>
</footer>

</body>
</html>
```